Family Brewery needs a label design for the four different types of beer.

We need a label design for two beer bottle sizes (500 and 700 ml. )
The label design should include the family monogram and company logo, as it would be a corporate gift for the new year from our CEO to business partners and clients. We have one request for showing the company logo on bottle. As it would be the new year edition, we would like to see design "adaptive" in case we would like to keep it after the holidays on an ongoing basis. Our main company direction is design and manufacture of cooling equipment for ice rinks, so it would be fine but not necessary to see design related to our business (if you would like to check the company, there is our website - www.velmarik.ru)
Labels on bottles should be in the same style but vary depending on the variety and taste of beer.
Types of bear
-Pilzner ( 4.4 % of alcohol)
-Honig Pilsner(5.2 % of alcohol)
-Wiener Ale ( 4.7 % of alcohol)
-Weissbier (5.6 % of alcohol)
If you have any questions just message me and i will answer as soon as possible.
Files attached contain the family monogram, company logo ( velmarik ), picture of beer bottles that would be in usage.

```html
<!DOCTYPE html>
<html lang="en">
<head>
<meta charset="utf-8">
<title>Family Brewery — Pilzner Label</title>
<link rel="stylesheet" href="https://fonts.googleapis.com/css2?family=Oswald:wght@500;600&family=Roboto+Condensed:wght@300;400;700&display=swap">
<style>
  :root {
    --backdrop: #e9eaea;
    --label: #ffffff;
    --gold: #b0945c;
    --gold-soft: #e4d6b8;
    --gold-pale: #f3ecdc;
    --ink: #15161d;
  }
  html, body {
    margin: 0;
    padding: 0;
    overflow: hidden;
    background: var(--backdrop);
  }
  .canvas {
    width: 1200px;
    height: 1200px;
    display: block;
  }
  .label-body { fill: var(--label); }
  .rule { fill: none; stroke: var(--gold); }
  .rule--thick { stroke-width: 4; }
  .rule--thin { stroke-width: 1.6; }
  .band { fill: var(--label); stroke: var(--gold); stroke-width: 3; }
  .band-inner { fill: none; stroke: var(--gold); stroke-width: 1.5; }
  .arc-title {
    font-family: "Oswald", sans-serif;
    font-weight: 500;
    font-size: 50px;
    letter-spacing: 5px;
    fill: var(--ink);
  }
  .beer-name {
    font-family: "Oswald", sans-serif;
    font-weight: 600;
    font-size: 148px;
    letter-spacing: 4px;
    fill: var(--ink);
  }
  .spec {
    font-family: "Roboto Condensed", sans-serif;
    font-weight: 300;
    font-size: 22px;
    fill: var(--gold);
  }
  .spec--small { font-size: 13px; }
  .company-name {
    font-family: "Roboto Condensed", sans-serif;
    font-weight: 400;
    font-size: 24px;
    letter-spacing: 1px;
    fill: var(--gold);
  }
  .arc-maker {
    font-family: "Roboto Condensed", sans-serif;
    font-weight: 700;
    font-size: 46px;
    fill: var(--ink);
  }
</style>
</head>
<body>
<svg class="canvas" viewBox="0 0 1000 1000" xmlns="http://www.w3.org/2000/svg">
  <defs>
    <clipPath id="label-cut">
      <rect x="175" y="0" width="650" height="1000"/>
    </clipPath>
    <linearGradient id="ornament-tone" x1="0" x2="1" y1="0" y2="0">
      <stop offset="0" stop-color="var(--gold-pale)"/>
      <stop offset="0.5" stop-color="var(--gold-soft)"/>
      <stop offset="1" stop-color="var(--gold-pale)"/>
    </linearGradient>
    <path id="arc-top" d="M 178 562 A 322 322 0 0 1 822 562"/>
    <path id="arc-bottom" d="M 210 510 A 290 290 0 0 0 790 510"/>
  </defs>

  <!-- Label shape -->
  <circle class="label-body" cx="500" cy="497" r="368" clip-path="url(#label-cut)"/>

  <!-- Shield outline: upper arch -->
  <path class="rule rule--thick" d="M 212 318 A 341 341 0 0 1 788 318"/>
  <path class="rule rule--thin" d="M 224 318 A 334 334 0 0 1 776 318"/>

  <!-- Shield outline: lower arch -->
  <path class="rule rule--thick" d="M 212 665 A 329 329 0 0 0 788 665"/>
  <path class="rule rule--thin" d="M 224 665 A 321 321 0 0 0 776 665"/>

  <!-- Title arc -->
  <text class="arc-title" text-anchor="middle">
    <textPath href="#arc-top" startOffset="50%">FAMILY BREWERY</textPath>
  </text>

  <!-- Top band with monogram -->
  <rect class="band" x="205" y="318" width="585" height="84"/>
  <rect class="band-inner" x="214" y="327" width="567" height="66"/>
  <g role="img" aria-label="Family monogram with crown and floral scrollwork">
    <rect x="240" y="342" width="515" height="38" fill="url(#ornament-tone)"/>
    <circle cx="500" cy="360" r="48" fill="var(--gold-soft)" stroke="var(--gold)" stroke-width="3"/>
    <rect x="472" y="268" width="56" height="34" fill="var(--gold-soft)"/>
  </g>

  <!-- Beer name -->
  <text class="beer-name" x="500" y="560" text-anchor="middle">PILZNER</text>

  <!-- Lower band with specs -->
  <rect class="band" x="205" y="578" width="585" height="87"/>
  <rect class="band-inner" x="214" y="587" width="567" height="69"/>
  <text class="spec" x="313" y="622">500 ml</text>
  <text class="spec" x="583" y="622">4.4 % <tspan class="spec--small">of alcohol</tspan></text>
  <text class="company-name" x="497" y="630" text-anchor="middle">VELMARIK</text>

  <!-- Maker arc -->
  <text class="arc-maker" text-anchor="middle">
    <textPath href="#arc-bottom" startOffset="50%">Велмарик-Л | Velmarik-L</textPath>
  </text>
</svg>
</body>
</html>
```